Business Card Design Project

Use newly designed logo and tie into newly designed website
I need a new logo and website layout designed for my partner's business. This is a birthday present. His business is interior painting, wallpapering and design. He also has access to a wide variety of products including carpet, fabrics, furniture, wallpaper, tile, countertops, etc. I have attached some screen shots of his website for reference. He is a one man shop and has a stellar reputation with his customers. He is on-time, very tidy, excellent with animals, and always finishes on time and on budget. There are no restrictions on colors or fonts. The logo needs to work well with the website, business cards and printed materials. The website needs to flow content for device size so it looks just as good on a cell phone or tablet as it does on a desktop computer. Whatever the heck that's called!Thanks. I am looking forward to seeing everyone's ideas.
Updates
Hi Designers,
We've reopened this project as our logo design project has just completed.
Please refer to the uploaded files and make use of either Horizontal or Vertical versions of the logo depending on what you think is suitable for your design proposals.
We look forward to your creative submissions!
Target Market(s)
Consumers looking to improve the interior environment of their homes by updating wall paint or paper, flooring (either carpet, tile, or hardwoods), counter tops, window treatments, etc. Clients tend to be more upper middle class and have certain taste levels and expectations. New logo, website and business card should align to meet those levels.
Industry/Entity Type
Cell Phone
Look and feel
Each slider illustrates characteristics of the customer's brand and the style your logo design should communicate.

```html
<!DOCTYPE html>
<html lang="en">
<head>
<meta charset="utf-8">
<title>Verano Interior Designs – Business Card</title>
<link rel="stylesheet" href="https://fonts.googleapis.com/css2?family=Open+Sans:wght@400;600;700&display=swap">
<style>
  :root {
    --stage: #4a4a4a;
    --card: #f6f8f7;
    --brand-dark: #7f2f1d;
    --band-top: #a95f2b;
    --band-bottom: #8b3b20;
    --divider: #c7794a;
    --white: #ffffff;
    --address: #555a5c;
  }
  * { margin: 0; padding: 0; box-sizing: border-box; }
  html, body {
    width: 1200px; height: 999px; overflow: hidden;
    background: var(--stage);
    font-family: "Open Sans", Arial, sans-serif;
  }
  .business-card {
    position: absolute; left: 75px; top: 199px;
    width: 1050px; height: 600px;
    background: var(--card);
  }
  .brand {
    position: absolute; left: 0; right: 0; top: 82px;
    display: flex; justify-content: center; align-items: center; gap: 22px;
    color: var(--brand-dark); font-weight: 600;
  }
  .brand-mark {
    width: 30px; height: 30px; border-radius: 50%;
    background: var(--brand-dark);
  }
  .brand-name { line-height: 1; }
  .brand-name .primary { display: block; font-size: 66px; letter-spacing: 1px; }
  .brand-name .secondary { display: block; font-size: 38px; margin-top: 8px; }
  .contact-band {
    position: absolute; left: 0; top: 300px; width: 100%; height: 158px;
    background: linear-gradient(to bottom, var(--band-top), var(--band-bottom));
    color: var(--white);
  }
  .band-divider {
    position: absolute; left: 500px; top: 6px; width: 1px; height: 146px;
    background: var(--divider);
  }
  .person {
    position: absolute; right: 597px; top: 42px; text-align: right;
  }
  .person .name { font-size: 36px; font-weight: 700; line-height: 1.1; }
  .person .role { font-size: 24px; line-height: 1.3; }
  .contact-list {
    position: absolute; left: 531px; top: 38px; list-style: none;
    font-size: 23px; line-height: 30.5px;
  }
  .contact-list li { display: flex; align-items: center; gap: 16px; }
  .contact-list svg { width: 24px; height: 24px; flex: none; }
  .address {
    position: absolute; left: 0; right: 0; top: 470px; text-align: center;
    font-size: 22px; color: var(--address);
  }
</style>
</head>
<body>
  <div class="business-card">
    <div class="brand">
      <span class="brand-mark"></span>
      <div class="brand-name">
        <span class="primary">Verano</span>
        <span class="secondary">Interior Designs</span>
      </div>
    </div>

    <div class="contact-band">
      <div class="person">
        <div class="name">Title name</div>
        <div class="role">designation</div>
      </div>
      <div class="band-divider"></div>
      <ul class="contact-list">
        <li>
          <svg viewBox="0 0 24 24" aria-hidden="true"><rect x="4" y="2" width="16" height="20" rx="3" fill="#fff"/><rect x="7" y="5" width="10" height="12" fill="#9a4a25"/></svg>
          (555) 214-0391
        </li>
        <li>
          <svg viewBox="0 0 24 24" aria-hidden="true"><rect x="2" y="9" width="20" height="13" rx="2" fill="#fff"/><path d="M2 10 L12 3 L22 10" fill="#fff"/><path d="M3 11 L12 17 L21 11" fill="none" stroke="#9a4a25" stroke-width="1.6"/></svg>
          dale@veranointeriors.com
        </li>
        <li>
          <svg viewBox="0 0 24 24" aria-hidden="true" fill="none" stroke="#fff" stroke-width="2"><circle cx="12" cy="12" r="10" fill="#fff"/><g stroke="#964624" stroke-width="1.4"><ellipse cx="12" cy="12" rx="4" ry="9"/><line x1="3" y1="12" x2="21" y2="12"/><line x1="5" y1="7" x2="19" y2="7"/><line x1="5" y1="17" x2="19" y2="17"/></g></svg>
          www.veranointeriors.com
        </li>
      </ul>
    </div>

    <p class="address">Dale Verano 2810 W Linden Ct. Fairview, KS 66000</p>
  </div>
</body>
</html>
```